Larkfield Property Maintenance needs a logo and business card

Maintenance company providing Residential/Commercial small building and maintenance works.This start up company needs a professional image with a new logo/business card.

The company name is 'Larkfield Property Maintenance'

The logo/business card should use the colour ORANGE.

Would like solid colour orange with logo on one side.
Name and business details on the other.

I would like a picture of a 'house' as part of the logo.

Need to be professional and classy but with a slightly softer edge to appeal to female as well as male clients.

The text on the card and tag line for the business to be included on the card as follows:

"Larkfield Property Maintenance
A commitment to quality with exceptional service ..."

Declan Whitby

(Icons for Ph. Email. Mob. and Web address)

MOB. 0412 578 319
PH. 03 9617 2248
Email: declan@larkfieldpropertymaintenance.com.au
Address: 47 Tilbury Lane, Ashvale North VIC 3178
Web: larkfieldpropertymaintenance.com.au

Target Market(s)

35 to 55 year old time poor professional white collar

Industry/Entity Type

Building

Logo Text

Larkfield Property Maintenance (tag line: A Commitment to Quality and Exceptional Service)

Font styles to use
Sans Serif

Requirements
Must have
• The logo picture should be of a house
Should not have
• Do not want references to orange 'fruit' in the design

```html
<!DOCTYPE html>
<html lang="en">
<head>
<meta charset="utf-8">
<title>Larkfield Property Maintenance — Business Card</title>
<link rel="stylesheet" href="https://fonts.googleapis.com/css2?family=Open+Sans:ital,wght@0,400;0,600;0,700;1,400&display=swap">
<style>
  :root {
    --backdrop: #6b6c6f;
    --orange: #f18a21;
    --orange-soft: #fbe3cc;
    --white: #ffffff;
    --ink: #3a3a3a;
  }
  html, body {
    margin: 0;
    padding: 0;
    width: 988px;
    height: 1200px;
    overflow: hidden;
    background: var(--backdrop);
    font-family: "Open Sans", Arial, sans-serif;
  }
  .stage {
    position: relative;
    width: 988px;
    height: 1200px;
  }
  .card {
    position: absolute;
    left: 202px;
    width: 602px;
    height: 350px;
    overflow: hidden;
  }
  .card--front {
    top: 191px;
    background: var(--orange);
    color: var(--white);
    text-align: center;
  }
  .brand {
    position: absolute;
    left: 0;
    right: 0;
    top: 86px;
  }
  .brand__mark {
    display: block;
    margin: 0 auto 16px;
    width: 36px;
    height: 36px;
    border-radius: 50%;
    background: var(--white);
  }
  .brand__name {
    margin: 0;
    font-weight: 600;
    color: var(--white);
    line-height: 1;
  }
  .brand__name-main {
    display: block;
    font-size: 40px;
    letter-spacing: 6px;
    padding-left: 6px;
  }
  .brand__name-sub {
    display: block;
    margin-top: 7px;
    font-size: 16px;
    letter-spacing: 2.4px;
  }
  .tagline {
    position: absolute;
    left: 0;
    right: 0;
    top: 250px;
    margin: 0;
    font-size: 14px;
    font-style: italic;
    letter-spacing: -0.2px;
  }
  .card--back {
    top: 663px;
    background: var(--white);
    color: var(--ink);
  }
  .backdrop-disc {
    position: absolute;
    left: 488px;
    top: 204px;
    width: 150px;
    height: 150px;
    border-radius: 50%;
    background: var(--orange-soft);
    opacity: 0.8;
  }
  .person {
    position: absolute;
    left: 54px;
    top: 58px;
    margin: 0;
    font-size: 22px;
    font-weight: 700;
    color: var(--orange);
  }
  .address {
    position: absolute;
    left: 56px;
    top: 96px;
    margin: 0;
    font-style: normal;
    font-size: 16px;
    line-height: 26px;
    font-weight: 600;
  }
  .contacts {
    position: absolute;
    left: 195px;
    top: 236px;
    margin: 0;
    padding: 0;
    list-style: none;
    font-size: 15.5px;
    line-height: 18px;
  }
  .contacts li {
    display: flex;
    align-items: center;
    gap: 12px;
  }
  .contacts svg {
    width: 11px;
    height: 11px;
    fill: var(--orange);
    flex: none;
  }
</style>
</head>
<body>
<main class="stage">
  <section class="card card--front" aria-label="Business card front">
    <div class="brand">
      <span class="brand__mark" aria-hidden="true"></span>
      <h1 class="brand__name">
        <span class="brand__name-main">LARKFIELD</span>
        <span class="brand__name-sub">Property Maintenance</span>
      </h1>
    </div>
    <p class="tagline">A Commitment to Quality and Exceptional Service</p>
  </section>

  <section class="card card--back" aria-label="Business card back">
    <span class="backdrop-disc" aria-hidden="true"></span>
    <h2 class="person">Declan Whitby</h2>
    <address class="address">47 Tilbury Lane,<br>Ashvale North VIC 3178</address>
    <ul class="contacts">
      <li>
        <svg viewBox="0 0 12 12" aria-hidden="true"><path d="M2.5 0.8l2 2.2-1 1.3c.7 1.6 2 2.9 3.6 3.6l1.3-1 2.2 2-1.2 2.1C5 10.6 1.4 7 .4 2z"/></svg>
        <span>03 9617 2248</span>
      </li>
      <li>
        <svg viewBox="0 0 12 12" aria-hidden="true"><path d="M3.5 0h5a1 1 0 0 1 1 1v10a1 1 0 0 1-1 1h-5a1 1 0 0 1-1-1V1a1 1 0 0 1 1-1zm.5 1.5v7.5h4V1.5z"/></svg>
        <span>0412 578 319</span>
      </li>
      <li>
        <svg viewBox="0 0 12 12" aria-hidden="true"><path d="M0 2.5h12v7H0zM1 3.3l5 3.4 5-3.4v-.3H1z"/></svg>
        <span>declan@larkfieldpropertymaintenance.com.au</span>
      </li>
      <li>
        <svg viewBox="0 0 12 12" aria-hidden="true"><path d="M6 0.8L0.5 5.8h1.7V11h3V7.8h1.6V11h3V5.8h1.7z"/></svg>
        <span>larkfieldpropertymaintenance.com.au</span>
      </li>
    </ul>
  </section>
</main>
</body>
</html>
```